Guarenteed! - Homepage Website Design - Coding not required- Winner to complete further pages

Hi all,

We're looking at redesigning our current website with a few adjustments to other pages but the main adjustments will be on the homepage which is what this design request is for. Please note : any of these ideas can be changed if you have something particularly different / special in mind etc.

P.S Coding is not required, just a design.

- Our website -

Our website is simply a price comparison website that allows customers to find companies within their area at the best price. The products available are mostly related to the vehicle trade and all refer to vinyl. This includes the likes of vehicle window tint, vehicle colour change vehicle wrap, vehicle signage as well as other cosmetic vinyl modifications. We allow the customer to search for their product within their chosen area and receive a list of companies who supply their product within that area. From here they can compare prices and view further details on the company.

- What we're looking to do -

We're looking first of all to adjust how the website homepage is displayed, this includes adding images and adjusting the colours that are explained below:

First of all, we look to spread out each of the 12 products (which can be seen on the website as it stands) and add an image to each of the products (all being spaced out as shown in our sketch)

We've been told the website looks too busy so we're thinking if we adjust the colours to more simplier neutral colours as well as the main focus of the website being on the 12 images, that would be great.

- Logo + Banner -

Logo to remain top left although banner may be removed / adjusted to make simplier.

- Colours -

Adjustments - Colours shades
We want the website to still look exciting but simplify the colours. Needs to be kept up to date with the colours / textures etc (bright colours to highlight keypoints)
We're still looking to use either blue or orange or maybe both to highlight these keypoints but the main website to be light colours and maybe even black on white background. The entire homepage can be adjusted colour wise if you feel it fits into your theme including menu bars, banners etc. The key is to get this right with being not too overpowering with the colours but still look interesting and up to date.

- 1 - 4 steps banner - (text may change)

This sits just under the logo and explains to the user how easy the website is to use and the steps they need to take. This may change to a 1 - 5 steps but we're looking to have this designed once the overall colours / theme of the website is sorted.

- 12 images - 4 x 3

This is the main focus of the website and will be the main focus of what the customer sees first of all. This will be where they select their product and then underneath, enter their postcode and distance they would like to search within. As explained further up, we have some of the product images available so if you can where possible add these to the design and then duplicate the images on those we currently don't have available.

- 12 Images -Titles -

These titles will be in this order from left to right and etc

- Colour Change Wrap
- Printed Vehicle Wrap
- Window Tint
- Headlight Tint
- Vehicle Signage
- Shop Signage
- Roof Vinyl Wrap
- Bonnet Vinyl Wrap
- Carbon Fibre Vinyl
- Stickerbomb Vinyl
- Clear Protective Vinyl
- Wheel Refurb

Text to be quite large, centered and with the o to the left of the title. Short titles like 'Window Tint' should fit on one line in the middle of the box where as titles such as ' Stickerbomb Vinyl Wrap' should have the 'Stickerbomb Vinyl' on the first line with the 'Wrap' on the line below. The background of this text is up to experient, might be worth just a simple colour or it might be worth using a bright blue or orange to keep in with the theme of the logo etc.

These will also have the circle tick box to the left of the title (as on the current website) where the customer clicks to select the product they have available.
We were also thinking that if when the customer ticks the circle on their selected box, the box is highlighted in some way to show this.

- Search Block -

This will appear under the 12 images and allows the customer to input their postcode and distance for the search criteria. Colours on this can of course be adjusted to keep in theme with the website.

- Under the 12 Images -

- Block underneath the 12 images and search block -

To the left will be some key bullet points about the website - maybe 4 or 5 with a green tick to the left of this. Background colour will probably be best to be a light colour, possibly grey.

Then to the right of this will appear 4 images, 2 before and 2 after when applying these products. Images to be used aren't fully decided on and we would like this stage of the design left to the end when the rest of the theme etc have been decided on.

Attached images are as follows :
- How the website looks as it stands
- The fold line on the website (obviously important)
- Our rough sketch of how we'd like the website homepage to look.
- We have 7 of the images ready that are all attached in this one file. Please duplicate the images on those that currently don't have the image available.

We will also be requesting a website developer to put this into action if our current designer falls through so please feel free to contact us if potentially interested.

The layout can change if you can think of something particular different / unique that works with this design. The main idea is to not only get the 12 products on view to the viewers but also the keypoints and before and after images.

Any questions, please ask away as we're bound to have forgotten a few things.

Thanks and good luck!

Hi all, keep the designs coming.

We haven't quite seen that extra special design we're after. As stated, we're after something fairly simple to suit the youth as well as the middle aged but we're also after something that bit special.

Colours to concentrate on are still and orange etc although feel free to use other colours if you have anything special in mind.

Please experience and we'll give you our honest feedback.

Many thanks all and good luck!

Hi all, this is a message to all the designers.

Some good designs coming in but we're still after that something special for the website design. Keep the designs coming and please feel free to experiment with the design colours, layout etc.

The basic principle of the website needs to remain regarding the 12 products, search within block and 4 steps all appearing on the homepage.

The 4 steps seems to work best when it's got text as well as some simple images next to this.

A variation with the product titles with how to display this, some designers have gone with a simple white background whereas others have gone with colours. Please experiment here and where possible, add a contract / texture to the colour. Please remember the product titles needs to be clear, centured and with the circle tick box to the left of it. 

We're after a fairly simple design although we need it to look 21st century, up to date as well as interesting. The key points straight away are the 4 steps as well as the 12 products so try to guide the viewer to these areas a little.

White background behind the 12 images seems to be a much, although a light colour could possibly work.

The keypoints underneath these 12 products are too very important as it outlines what we do etc. Tick colour can vary.

Next to these keypoints will be the 'before' and 'after' images, these images needs to be fairly small and ensure there is white background around the image itself.

Good luck all and any questions, feel free to ask away.

Thanks!

Hi,

 Thank you for your time and effort with these designs, we are very nearly there with the design but we've thought of something that may work for the homepage. A curved arrow from step 1 pointing to the products, this may or may not work but feel free to give it a go.

Many thanks,

Thank you to everyone for your time and efforts with the design. It's hugely appreciated so thank you all once again.

Wish you all the luck in the future.

```html
<!DOCTYPE html>
<html lang="en">
<head>
<meta charset="utf-8">
<title>Comparison Steps – Interaction Notes</title>
<link rel="stylesheet" href="https://fonts.googleapis.com/css2?family=Gochi+Hand&family=Questrial&display=swap">
<style>
  :root {
    --orange: #f7931e;
    --orange-deep: #ef7d00;
    --orange-text: #f08300;
    --orange-soft: #fde3c2;
    --orange-pale: #fff6ec;
    --muted: #c4ccd9;
    --muted-icon: #b9c3d2;
    --line: #c9d4e2;
    --strip-top: #f6f8fb;
    --strip-bottom: #dfe6ef;
    --note: #6b6b6b;
    --field-text: #7f98c7;
    --blue-btn-top: #dbe6f7;
    --blue-btn-bottom: #8ea9d9;
    --blue-btn-text: #2f4b86;
    --white: #ffffff;
  }
  * { box-sizing: border-box; margin: 0; padding: 0; }
  html, body { width: 1200px; height: 840px; overflow: hidden; background: var(--white); }
  .sheet {
    position: relative; width: 1000px; height: 700px;
    transform: scale(1.2); transform-origin: 0 0;
    font-family: "Questrial", "Century Gothic", sans-serif;
  }
  .note {
    position: absolute; font-family: "Gochi Hand", cursive; font-style: italic;
    color: var(--note); font-size: 19px; line-height: 22px; letter-spacing: 1.35px; white-space: nowrap;
  }
  .pointer { position: absolute; overflow: visible; }

  /* step bar */
  .step-bar { position: absolute; left: 30px; width: 938px; height: 97px; }
  .tab {
    position: absolute; top: 0; height: 27px; width: 236px;
    background: linear-gradient(#ffb347, var(--orange));
    border-radius: 7px 7px 0 0; color: var(--white);
    font-size: 16px; display: flex; align-items: center; padding-left: 10px; gap: 8px; z-index: 2;
  }
  .tab-num {
    width: 18px; height: 18px; border-radius: 50%; border: 2px solid var(--white);
    display: flex; align-items: center; justify-content: center; font-weight: 700; font-size: 13px;
  }
  .strip {
    position: absolute; top: 10px; height: 17px;
    background: linear-gradient(var(--strip-top), var(--strip-bottom));
    border: 1px solid var(--line); border-bottom: none; border-radius: 0 6px 0 0;
  }
  .cells {
    position: absolute; top: 27px; left: 0; right: 0; height: 71px;
    display: flex; border: 1px solid var(--line);
  }
  .cell {
    position: relative; flex: 1; border-right: 1px solid var(--line);
    background: linear-gradient(var(--white), var(--orange-pale) 60%, #fdecd8);
    color: var(--muted);
  }
  .cell:last-child { border-right: none; }
  .cell.is-active { background: linear-gradient(#fff3e2, var(--orange-soft)); color: var(--orange-text); }
  .corner {
    position: absolute; left: 0; top: 0; width: 0; height: 0;
    border-top: 18px solid #eadfd2; border-right: 18px solid transparent;
  }
  .corner-num { position: absolute; left: 2px; top: -1px; font-size: 11px; color: #8c8c8c; }
  .cell-label {
    position: absolute; left: 18px; top: 13px; font-style: italic; font-size: 17.5px; line-height: 21px;
  }
  .is-active .cell-label::after {
    content: ""; position: absolute; left: 0; right: -10px; bottom: -7px; height: 2px; background: var(--orange-deep);
  }
  .cell-icon { position: absolute; right: 20px; top: 9px; width: 54px; height: 54px; }
  .is-active .corner { display: none; }

  /* search panel */
  .search-panel { position: absolute; width: 939px; height: 98px; }
  .search-body {
    position: absolute; top: 26px; left: 0; right: 0; height: 72px; display: flex;
    border: 1px solid var(--line); background: linear-gradient(var(--white), var(--orange-pale) 70%, #fdebd6);
  }
  .search-half { position: relative; display: flex; align-items: center; }
  .search-half:first-child { width: 396px; border-right: 1px solid var(--line); padding-left: 42px; gap: 18px; }
  .search-half:last-child { flex: 1; padding-left: 42px; gap: 12px; }
  .search-label { color: var(--orange-deep); font-size: 15px; }
  .field {
    height: 26px; border: 1px solid #f4b860; background: var(--white);
    font-style: italic; font-size: 14px; color: var(--field-text); display: flex; align-items: center; padding-left: 12px;
  }
  .field-postcode { width: 152px; }
  .field-distance { width: 152px; justify-content: space-between; padding-right: 0; }
  .select-arrow { width: 34px; height: 24px; background: #e9eef5; display: flex; align-items: center; justify-content: center; }
  .search-btn {
    margin-left: auto; margin-right: 40px; width: 135px; height: 34px; border-radius: 17px;
    background: linear-gradient(var(--blue-btn-top), var(--blue-btn-bottom));
    box-shadow: 0 2px 3px rgba(0,0,0,.25);
    color: var(--blue-btn-text); font-style: italic; font-weight: 700; font-size: 17px;
    display: flex; align-items: center; justify-content: center; gap: 6px;
  }
  .search-panel.is-focused .strip { background: linear-gradient(#ffc26e, var(--orange)); border-color: var(--orange-deep); }
  .search-panel.is-focused .search-body { border-color: var(--orange-deep); background: linear-gradient(var(--white), #fff0dc 70%, #fde0b8); }
  .search-panel.is-focused .search-half:first-child { border-right-color: var(--orange-deep); }
  .search-panel.is-focused .field { color: var(--orange); }
  .search-panel.is-focused .select-arrow { background: #fbe9cf; }
  .search-panel.is-focused .search-btn {
    background: linear-gradient(#ffe0a8, var(--orange)); color: var(--orange-deep);
  }
  .search-panel.is-focused .corner { border-top-color: #fbd3a0; }
</style>
</head>
<body>
<div class="sheet">

  <p class="note" style="left:37px; top:7px;">Starts like this:</p>

  <section class="step-bar" style="top:34px;">
    <div class="tab" style="left:0;"><span class="tab-num">1</span>Start Comparison Here!</div>
    <div class="strip" style="left:236px; right:0;"></div>
    <div class="cells">
      <div class="cell is-active">
        <span class="cell-label">Select Your<br>Chosen Product</span>
        <svg class="cell-icon" viewBox="0 0 54 54" fill="var(--orange)"><path d="M17 24v-8a10 10 0 0 1 20 0v8h-4v-8a6 6 0 0 0-12 0v8z"/><rect x="12" y="23" width="30" height="28" rx="3"/></svg>
      </div>
      <div class="cell">
        <span class="corner"></span><span class="corner-num">2</span>
        <span class="cell-label">Input Location<br>&amp; Search</span>
        <svg class="cell-icon" viewBox="0 0 54 54" fill="none" stroke="var(--muted-icon)"><circle cx="22" cy="22" r="13" stroke-width="6"/><path d="M32 32l14 14" stroke-width="8" stroke-linecap="round"/></svg>
      </div>
      <div class="cell">
        <span class="corner"></span><span class="corner-num">3</span>
        <span class="cell-label">Compare<br>Firms &amp; Prices</span>
        <svg class="cell-icon" viewBox="0 0 54 54" role="img" aria-label="Strategy board icon"><rect x="2" y="2" width="50" height="50" rx="3" fill="var(--muted-icon)"/></svg>
      </div>
      <div class="cell">
        <span class="corner"></span><span class="corner-num">4</span>
        <span class="cell-label">Contact Your<br>Chosen Company</span>
        <svg class="cell-icon" viewBox="0 0 54 54" fill="var(--muted-icon)"><rect x="34" y="2" width="4" height="12"/><rect x="16" y="10" width="24" height="42" rx="4"/><rect x="20" y="15" width="16" height="12" fill="#fff"/><g fill="#fff"><rect x="20" y="31" width="4" height="3"/><rect x="26" y="31" width="4" height="3"/><rect x="32" y="31" width="4" height="3"/><rect x="20" y="37" width="4" height="3"/><rect x="26" y="37" width="4" height="3"/><rect x="32" y="37" width="4" height="3"/><rect x="20" y="43" width="4" height="3"/><rect x="26" y="43" width="4" height="3"/><rect x="32" y="43" width="4" height="3"/></g></svg>
      </div>
    </div>
  </section>

  <svg class="pointer" style="left:258px; top:138px;" width="20" height="14" fill="none" stroke="#777" stroke-width="1"><path d="M2 12L18 2M12 2h6v5"/></svg>
  <p class="note" style="left:37px; top:151px;">On click the page would auto scroll (and expand / minimize sections as neccessary) to the next section</p>
  <svg class="pointer" style="left:500px; top:182px;" width="20" height="14" fill="none" stroke="#777" stroke-width="1"><path d="M18 2L2 12M2 6v6h6"/></svg>
  <p class="note" style="left:520px; top:172px;">And the bar transitions to the next like shown</p>

  <section class="step-bar" style="top:194px;">
    <div class="strip" style="left:0; right:0; border-radius:6px 6px 0 0;"></div>
    <div class="tab" style="left:236px; width:235px;"><span class="tab-num">2</span>Step 2: search!</div>
    <div class="cells">
      <div class="cell">
        <span class="corner"></span><span class="corner-num">1</span>
        <span class="cell-label">Select Your<br>Chosen Product</span>
        <svg class="cell-icon" viewBox="0 0 54 54" fill="var(--muted-icon)"><path d="M17 24v-8a10 10 0 0 1 20 0v8h-4v-8a6 6 0 0 0-12 0v8z"/><rect x="12" y="23" width="30" height="28" rx="3"/></svg>
      </div>
      <div class="cell is-active">
        <span class="cell-label">Input Location<br>&amp; Search</span>
        <svg class="cell-icon" viewBox="0 0 54 54" fill="none" stroke="var(--orange)"><circle cx="22" cy="22" r="13" stroke-width="6"/><path d="M32 32l14 14" stroke-width="8" stroke-linecap="round"/></svg>
      </div>
      <div class="cell">
        <span class="corner"></span><span class="corner-num">3</span>
        <span class="cell-label">Compare<br>Firms &amp; Prices</span>
        <svg class="cell-icon" viewBox="0 0 54 54" role="img" aria-label="Strategy board icon"><rect x="2" y="2" width="50" height="50" rx="3" fill="var(--muted-icon)"/></svg>
      </div>
      <div class="cell">
        <span class="corner"></span><span class="corner-num">4</span>
        <span class="cell-label">Contact Your<br>Chosen Company</span>
        <svg class="cell-icon" viewBox="0 0 54 54" fill="var(--muted-icon)"><rect x="34" y="2" width="4" height="12"/><rect x="16" y="10" width="24" height="42" rx="4"/><rect x="20" y="15" width="16" height="12" fill="#fff"/><g fill="#fff"><rect x="20" y="31" width="4" height="3"/><rect x="26" y="31" width="4" height="3"/><rect x="32" y="31" width="4" height="3"/><rect x="20" y="37" width="4" height="3"/><rect x="26" y="37" width="4" height="3"/><rect x="32" y="37" width="4" height="3"/><rect x="20" y="43" width="4" height="3"/><rect x="26" y="43" width="4" height="3"/><rect x="32" y="43" width="4" height="3"/></g></svg>
      </div>
    </div>
  </section>

  <p class="note" style="left:33px; top:309px;">At which point the search box receive focus &amp; could change from something like below</p>
  <svg class="pointer" style="left:275px; top:336px;" width="20" height="14" fill="none" stroke="#777" stroke-width="1"><path d="M18 2L2 12M2 6v6h6"/></svg>

  <section class="search-panel" style="left:23px; top:343px;">
    <div class="tab" style="left:0;"><span class="tab-num">2</span>Input Location &amp; Search</div>
    <div class="strip" style="left:236px; right:0;"></div>
    <div class="search-body">
      <div class="search-half">
        <span class="corner"></span><span class="corner-num">1</span>
        <span class="search-label">Postcode:</span>
        <span class="field field-postcode">enter here...</span>
      </div>
      <div class="search-half">
        <span class="corner"></span><span class="corner-num">2</span>
        <span class="search-label">Distance:</span>
        <span class="field field-distance">5 km<span class="select-arrow"><svg width="16" height="12"><path d="M0 0h16L8 12z" fill="#9aa7bb"/></svg></span></span>
        <span class="search-btn">Search! <svg width="22" height="22" fill="none" stroke="#fff" stroke-width="3"><circle cx="13" cy="9" r="6"/><path d="M9 13L3 19" stroke-linecap="round"/></svg></span>
      </div>
    </div>
  </section>

  <p class="note" style="left:42px; top:454px;">to something like this, which catches the eye more</p>
  <svg class="pointer" style="left:480px; top:478px;" width="20" height="14" fill="none" stroke="#777" stroke-width="1"><path d="M18 2L2 12M2 6v6h6"/></svg>

  <section class="search-panel is-focused" style="left:30px; top:499px;">
    <div class="tab" style="left:0;"><span class="tab-num">2</span>Input Location &amp; Search</div>
    <div class="strip" style="left:236px; right:0;"></div>
    <div class="search-body">
      <div class="search-half">
        <span class="corner"></span><span class="corner-num">1</span>
        <span class="search-label">Postcode:</span>
        <span class="field field-postcode">enter here...</span>
      </div>
      <div class="search-half">
        <span class="corner"></span><span class="corner-num">2</span>
        <span class="search-label">Distance:</span>
        <span class="field field-distance">5 km<span class="select-arrow"><svg width="16" height="12"><path d="M0 0h16L8 12z" fill="var(--orange)"/></svg></span></span>
        <span class="search-btn">Search! <svg width="22" height="22" fill="none" stroke="#fff" stroke-width="3"><circle cx="13" cy="9" r="6"/><path d="M9 13L3 19" stroke-linecap="round"/></svg></span>
      </div>
    </div>
  </section>

  <p class="note" style="left:52px; top:634px;">Please note the reason for using the yellow orange hues like this is to be in keeping with your logo</p>
  <p class="note" style="left:52px; top:656px;">if you want something else thats fine but bear in mind your logo may look out of place then</p>

</div>
</body>
</html>
```